Velumin clinic business card - double sided for young clinic

I require business cards for my aesthetic clinic specialising in the below treatments. I would like the cards to be modern as my clinic base are young 22-35 years old. I require my logo on it and would like the edges to be rounded.

I have an aesthetic clinic specialising in :
Velumin
Lip Enhancement
Chemical Peels
Facial Fillers
Non Surgical Face Lift

I would the cards to have the following information on them:
My logo - (in grey/silver)
address
Phone number
services

Colours :
White/grey/silver and red

a nice image on there, perhaps a set of lips as this is a main service i deliver

Company Name: HFA Address: 52 Harwell Lane, 4 Brimfold High Street, TN7 4QW Phone: 0207 948 2176 Website: www.helenfosburyaesthetics-example.co.uk

Target Market(s)

clinics 22-45 years old mainly female

Industry/Entity Type

Business

Contact Information for Business Card

as above

Requirements
Must have
• logo
• Address
• Email
• Phone number
• Services i offer
Nice to have
• images

```html
<!DOCTYPE html>
<html lang="en">
<head>
<meta charset="utf-8">
<title>HFA – Business Card</title>
<link rel="stylesheet" href="https://fonts.googleapis.com/css2?family=Arimo:wght@400;700&display=swap">
<style>
  :root {
    --page-bg: #e4e4e4;
    --card-grey: #a7a8aa;
    --band-grey: #a9aaac;
    --card-white: #ffffff;
    --ink-grey: #5d5e60;
    --logo-grey: #9d9ea0;
    --text-white: #ffffff;
  }
  * { box-sizing: border-box; margin: 0; padding: 0; }
  html, body {
    width: 1200px; height: 950px; overflow: hidden;
    background: var(--page-bg);
    font-family: "Arimo", Arial, sans-serif;
  }
  .canvas { position: relative; width: 1200px; height: 950px; }
  .card {
    position: absolute; left: 250px; width: 700px; height: 400px;
    border-radius: 18px; overflow: hidden;
    box-shadow: 0 6px 18px rgba(0,0,0,0.12);
  }
  /* Back side */
  .card-back { top: 60px; background: var(--card-grey); color: var(--text-white); }
  .back-logo {
    position: absolute; left: 90px; top: 140px;
    display: flex; align-items: center; gap: 18px;
  }
  .logo-dot { width: 34px; height: 34px; border-radius: 50%; flex: none; }
  .back-logo .logo-dot { background: var(--text-white); }
  .back-logo .logo-name { font-size: 58px; font-weight: 400; letter-spacing: 6px; color: var(--text-white); }
  .services { position: absolute; left: 400px; top: 110px; }
  .services-title { font-size: 22px; font-weight: 700; margin-bottom: 8px; }
  .services-list { list-style: none; font-size: 19px; line-height: 1.45; }
  .services-list li::before { content: "•"; margin-right: 9px; }

  /* Front side */
  .card-front { top: 500px; background: var(--card-white); color: var(--ink-grey); }
  .name-band {
    position: absolute; left: 0; top: 0; width: 100%; height: 92px;
    background: var(--band-grey); color: var(--text-white);
    padding: 22px 0 0 40px;
  }
  .person-name { font-size: 22px; font-weight: 700; }
  .person-role { font-size: 17px; margin-top: 4px; }
  .contact { position: absolute; left: 40px; top: 148px; font-size: 19px; line-height: 1.5; }
  .front-logo {
    position: absolute; right: 40px; top: 118px;
    display: flex; align-items: center; gap: 14px;
  }
  .front-logo .logo-dot { background: var(--logo-grey); }
  .front-logo .logo-name {
    font-size: 26px; font-weight: 400; letter-spacing: 3px;
    text-transform: uppercase; color: var(--logo-grey);
  }
  .address {
    position: absolute; right: 40px; bottom: 38px;
    text-align: right; font-size: 21px; line-height: 1.4;
  }
</style>
</head>
<body>
<main class="canvas">
  <section class="card card-back" aria-label="Business card back">
    <div class="back-logo">
      <span class="logo-dot"></span>
      <span class="logo-name">HFA</span>
    </div>
    <div class="services">
      <h2 class="services-title">Specialising in</h2>
      <ul class="services-list">
        <li>Velumin</li>
        <li>Lip Enhancement</li>
        <li>Chemical Peels</li>
        <li>Facial Fillers</li>
        <li>Non Surgical Face Lift</li>
      </ul>
    </div>
  </section>

  <section class="card card-front" aria-label="Business card front">
    <div class="name-band">
      <p class="person-name">Sam Ardley</p>
      <p class="person-role">President</p>
    </div>
    <div class="contact">
      <p>0207 948 2176</p>
      <p>info@helenfosburyaesthetics-example.co.uk</p>
      <p>www.helenfosburyaesthetics-example.co.uk</p>
    </div>
    <div class="front-logo">
      <span class="logo-dot"></span>
      <span class="logo-name">Helen Fosbury Aesthetics</span>
    </div>
    <address class="address" style="font-style:normal">
      <p>52 Harwell Lane</p>
      <p>4 Brimfold High Street</p>
      <p>TN7 4QW</p>
    </address>
  </section>
</main>
</body>
</html>
```